Pest Control Company needs business card!

Hi there, we need a business card designed for our new Pest Control Company. Ideally this card will be simple, yet feel elegant and high end. We want to use the colours Orange, Black and White. Please see our attached logo for the exact colours.

Business card details:

Phone - 0461 275 804
Name - Gavin Holloway
Email - Info@steadfastverminguard.com.au

We would also like to include the following list with dot points:

SERVICES / INSPECTIONS

Termites, Wood Borers, Ants, Cockroaches, Spiders, Fleas, Mice, Rats, Bed Bugs, & More!

```html
<!DOCTYPE html>
<html lang="en">
<head>
<meta charset="utf-8">
<title>Steadfast Vermin Guard – Business Card</title>
<link rel="stylesheet" href="https://fonts.googleapis.com/css2?family=Montserrat:wght@400;500;700;800&display=swap">
<style>
  :root {
    --orange: #ec8a35;
    --black: #262626;
    --ink: #2a2622;
    --white: #f4f1ec;
    --backdrop: #b9b9b9;
  }
  * { box-sizing: border-box; margin: 0; padding: 0; }
  html, body { width: 1200px; height: 675px; overflow: hidden; }
  body {
    background: var(--backdrop);
    font-family: "Montserrat", sans-serif;
    position: relative;
  }
  .card {
    position: absolute;
    top: 187px;
    width: 525px;
    height: 300px;
    border-radius: 24px;
    overflow: hidden;
  }
  .card--front { left: 50px; background: var(--orange); color: var(--ink); }
  .card--back { left: 625px; background: var(--black); color: var(--white); }

  .brand {
    position: absolute;
    font-weight: 800;
    text-transform: uppercase;
    line-height: 0.95;
    letter-spacing: 0.5px;
  }
  .brand__mark {
    display: inline-block;
    width: 14px; height: 14px;
    border-radius: 50%;
    margin-left: 6px;
    vertical-align: middle;
  }
  .card--front .brand { left: 64px; top: 46px; font-size: 30px; color: var(--ink); }
  .card--front .brand__mark { background: var(--ink); }
  .card--back .brand { left: 150px; top: 58px; font-size: 34px; color: var(--orange); }
  .card--back .brand__mark { background: var(--orange); }

  .rule { position: absolute; height: 1px; }
  .card--front .rule { background: var(--ink); left: 40px; right: 40px; }
  .rule--top { top: 176px; }
  .rule--bottom { top: 262px; }

  .contact {
    position: absolute;
    display: flex;
    align-items: center;
    gap: 7px;
    font-size: 11.5px;
    font-weight: 500;
    white-space: nowrap;
  }
  .contact svg { width: 14px; height: 14px; fill: var(--ink); flex: none; }
  .contact--email { left: 44px; top: 190px; }
  .contact--phone { left: 300px; top: 238px; }

  .person { position: absolute; right: 44px; top: 204px; text-align: right; white-space: nowrap; }
  .person__name { font-size: 16px; font-weight: 500; text-transform: uppercase; letter-spacing: 0.3px; line-height: 1.1; }
  .person__role { font-size: 10.5px; margin-top: 1px; }

  .services {
    position: absolute;
    left: 30px; right: 30px;
    top: 196px;
  }
  .services__title {
    text-align: right;
    font-size: 11px;
    letter-spacing: 0.5px;
    margin-right: 30px;
    padding-bottom: 8px;
  }
  .services__rule { height: 1px; background: var(--orange); }
  .services__list {
    font-size: 10.5px;
    padding-top: 10px;
    white-space: nowrap;
  }
</style>
</head>
<body>
  <section class="card card--front" aria-label="Business card front">
    <div class="brand">Steadfast<br>Vermin<br>Guard<span class="brand__mark"></span></div>
    <div class="rule rule--top"></div>
    <div class="contact contact--email">
      <svg viewBox="0 0 16 16" aria-hidden="true"><path d="M1 3h14v10H1z M2 4.2v0.3l6 4.3 6-4.3v-0.3z" fill-rule="evenodd"/></svg>
      <span>Info@steadfastverminguard.com.au</span>
    </div>
    <div class="person">
      <div class="person__name">Gavin Holloway</div>
      <div class="person__role">Owner</div>
    </div>
    <div class="contact contact--phone">
      <svg viewBox="0 0 16 16" aria-hidden="true"><path d="M3 2l3 0 1 3-2 1.5a9 9 0 0 0 4.5 4.5L11 9l3 1v3a1 1 0 0 1-1 1A12 12 0 0 1 2 3a1 1 0 0 1 1-1z"/></svg>
      <span>0461 275 804</span>
    </div>
    <div class="rule rule--bottom"></div>
  </section>

  <section class="card card--back" aria-label="Business card back">
    <div class="brand">Steadfast<br>Vermin<br>Guard<span class="brand__mark"></span></div>
    <div class="services">
      <div class="services__title">SERVICES / INSPECTIONS</div>
      <div class="services__rule"></div>
      <div class="services__list">Termites, Wood Borers, Ants, Cockroaches, Spiders, Fleas, Mice, Rats, Bed Bugs, &amp; More!</div>
    </div>
  </section>
</body>
</html>
```